New Corporate Business Card - Velmorabelle

What we need:
We need a new corporate business card.
We want a new template that we can change by ourself.
We want business card modern and minimalist but that looks professional.
We will print it in 300 gr soft-touch.
Why not a white side with the logo and a red/grey side with the content?
Why not a grey side and a red side like our logo?
I am sure that you have better idea than ours that's the reason we come here.

Who we are:
We are a private label company in cosmetics based in Switzerland. We work in BtoB. We make skin care products for other brands.

Target Market(s)

B to B - Worldwide - any gender

Industry/Entity Type

Cosmetics

Contact Information for Business Card

Side 1:
Logo
Your Swiss Private Label Manufacturer or www.velmorabelle.ch

Side 2:
Name and surname (Example: Lucien Marchetaz)
Job Description (General Manager)
Telephone (+41 32 918 64 00)
Direct (+41 32 918 64 64)
Email (lucien.marchetaz@velmorabelle.ch)
Chemin des Prés-Fleuris 14, 2000 Neuchâtel, Switzerland
www.velmorabelle.ch

Font styles to use
Serif
Sans Serif

Requirements
Must have
• You can use 4 colors: white, red, grey and/or black .
Should not have
• Too much colors, too much things. We want it simple!

```html
<!DOCTYPE html>
<html lang="en">
<head>
<meta charset="utf-8">
<title>Velmorabelle — Business Card</title>
<link rel="stylesheet" href="https://fonts.googleapis.com/css2?family=Questrial&display=swap">
<style>
  :root {
    --backdrop: #3a3b3e;
    --brand-red: #e01f1b;
    --card-grey: #a9aaac;
    --ink-white: #ffffff;
    --divider: #ffffff;
  }
  * { box-sizing: border-box; margin: 0; padding: 0; }
  html, body {
    width: 1200px;
    height: 880px;
    overflow: hidden;
    background: var(--backdrop);
    font-family: "Questrial", "Century Gothic", sans-serif;
  }
  .canvas {
    position: relative;
    width: 1200px;
    height: 880px;
  }
  .card {
    position: absolute;
    width: 620px;
    height: 376px;
    border-radius: 26px;
    overflow: hidden;
  }

  /* Front side */
  .card--front {
    left: 80px;
    top: 50px;
    background: var(--brand-red);
    color: var(--ink-white);
  }
  .brand {
    position: absolute;
    left: 0; right: 0;
    top: 120px;
    display: flex;
    justify-content: center;
    align-items: center;
    gap: 16px;
  }
  .brand__square {
    width: 22px;
    height: 22px;
    background: var(--ink-white);
  }
  .brand__name {
    font-size: 46px;
    letter-spacing: 6px;
    font-weight: 400;
  }
  .front__web {
    position: absolute;
    left: 0; right: 0;
    bottom: 54px;
    text-align: center;
    font-size: 19px;
    letter-spacing: 1.5px;
  }

  /* Back side */
  .card--back {
    left: 500px;
    top: 454px;
    background: var(--card-grey);
    color: var(--ink-white);
  }
  .identity {
    position: absolute;
    left: 24px;
    width: 262px;
    top: 116px;
    text-align: right;
  }
  .identity__name {
    color: var(--brand-red);
    font-size: 24px;
    font-weight: 400;
    text-transform: uppercase;
    letter-spacing: 0.2px;
    line-height: 1.1;
    white-space: nowrap;
  }
  .identity__role {
    font-size: 17px;
    margin-top: 5px;
  }
  .divider {
    position: absolute;
    left: 300px;
    top: 92px;
    width: 1px;
    height: 118px;
    background: var(--divider);
  }
  .contacts {
    position: absolute;
    left: 316px;
    top: 96px;
    list-style: none;
    font-size: 14.5px;
    line-height: 27px;
  }
  .contacts li {
    display: flex;
    align-items: center;
    gap: 9px;
    white-space: nowrap;
  }
  .icon {
    width: 14px;
    height: 14px;
    flex: none;
    fill: var(--brand-red);
  }
  .address {
    position: absolute;
    left: 0; right: 0;
    bottom: 42px;
    display: flex;
    justify-content: center;
    align-items: center;
    gap: 10px;
    font-size: 16px;
    white-space: nowrap;
  }
  .address .icon { width: 17px; height: 17px; }
</style>
</head>
<body>
<main class="canvas">

  <section class="card card--front" aria-label="Business card, front side">
    <div class="brand">
      <span class="brand__square"></span>
      <span class="brand__name">Velmorabelle</span>
    </div>
    <p class="front__web">www.velmorabelle.ch</p>
  </section>

  <section class="card card--back" aria-label="Business card, back side">
    <div class="identity">
      <h1 class="identity__name">Lucien Marchetaz</h1>
      <p class="identity__role">General Manager</p>
    </div>

    <span class="divider"></span>

    <ul class="contacts">
      <li>
        <svg class="icon" viewBox="0 0 14 14" aria-hidden="true"><path d="M4 0h6a1.5 1.5 0 0 1 1.5 1.5v11A1.5 1.5 0 0 1 10 14H4a1.5 1.5 0 0 1-1.5-1.5v-11A1.5 1.5 0 0 1 4 0zm0 1.6v9.4h6V1.6zm3 10.2a.8.8 0 1 0 0 1.6.8.8 0 0 0 0-1.6z"/></svg>
        <span>+41 32 918 64 64</span>
      </li>
      <li>
        <svg class="icon" viewBox="0 0 14 14" aria-hidden="true"><path d="M3 .5l2.3 3-1.4 1.6a8 8 0 0 0 5 5l1.6-1.4 3 2.3-1.7 2.4C6 13.2.8 8 .6 2.2z"/></svg>
        <span>+41 32 918 64 00</span>
      </li>
      <li>
        <svg class="icon" viewBox="0 0 14 14" aria-hidden="true"><path d="M0 2.5h14v1L7 8 0 3.5zM0 5l7 4.5L14 5v6.5H0z"/></svg>
        <span>lucien.marchetaz@velmorabelle.ch</span>
      </li>
      <li>
        <svg class="icon" viewBox="0 0 14 14" aria-hidden="true"><path d="M7 0a7 7 0 1 0 0 14A7 7 0 0 0 7 0zm-.7 1.5v2.6H4.1c.5-1.4 1.3-2.4 2.2-2.6zm1.4 0c.9.2 1.7 1.2 2.2 2.6H7.7zM3.6 2.4A8 8 0 0 0 2.8 4.1H1.9a5.6 5.6 0 0 1 1.7-1.7zm6.8 0a5.6 5.6 0 0 1 1.7 1.7h-.9a8 8 0 0 0-.8-1.7zM1.5 5.4h1.1a9 9 0 0 0 0 3.2H1.5a5.6 5.6 0 0 1 0-3.2zm2.4 0h2.4v3.2H3.9a8 8 0 0 1 0-3.2zm3.8 0h2.4a8 8 0 0 1 0 3.2H7.7zm3.7 0h1.1a5.6 5.6 0 0 1 0 3.2h-1.1a9 9 0 0 0 0-3.2zM1.9 9.9h.9c.2.6.5 1.2.8 1.7a5.6 5.6 0 0 1-1.7-1.7zm2.2 0h2.2v2.6c-.9-.2-1.700-1.2-2.2-2.6zm3.6 0h2.2c-.5 1.4-1.3 2.4-2.2 2.6zm3.5 0h.9a5.6 5.6 0 0 1-1.7 1.7c.3-.5.6-1.1.8-1.7z"/></svg>
        <span>www.velmorabelle.ch</span>
      </li>
    </ul>

    <p class="address">
      <svg class="icon" viewBox="0 0 16 16" aria-hidden="true"><path d="M8 1l8 7h-2.4v7H9.8v-4.6H6.2V15H2.4V8H0z"/></svg>
      <span>Chemin des Prés-Fleuris 14, 2000 Neuchâtel, Switzerland</span>
    </p>
  </section>

</main>
</body>
</html>
```